Flyer for the Harvest Lantern Gathering 2018

Design a flyer for our annual conference with basic information about the conference: conference logo and year,

Location:
Dunmore Community Center (Downtown Portland)
482 Willowby Street, Portland, ME 04117,

Date:
August 24th, 25th and 26th, 2018
Start time 6:00PM

I would like the following three words added to the flyer. These words describe the vision of the conference:
Prophetic, Worship, Prayer

```html
<!DOCTYPE html>
<html lang="en">
<head>
<meta charset="utf-8">
<title>Harvest Lantern Gathering 2018 – Annual Conference</title>
<link rel="stylesheet" href="https://fonts.googleapis.com/css2?family=Bungee&family=Open+Sans:wght@800&family=Michroma&family=PT+Sans+Narrow:wght@700&family=Cabin:wght@700&display=swap">
<style>
  :root {
    --pink: #f4419c;
    --pink-mid: #f7a3cf;
    --white: #ffffff;
    --ink: #1d1d1d;
    --gold: #e9a614;
  }
  html, body {
    margin: 0;
    padding: 0;
    overflow: hidden;
    background: var(--white);
  }
  .flyer {
    position: relative;
    width: 940px;
    height: 1200px;
    overflow: hidden;
    background: linear-gradient(180deg, var(--pink) 0%, var(--pink) 5%, var(--pink-mid) 27%, #fde3f0 40%, var(--white) 48%, var(--white) 100%);
    text-align: center;
  }
  .flyer > * {
    position: absolute;
    left: 0;
    right: 0;
    margin: 0;
  }
  .title {
    top: 82px;
    font-family: "Bungee", sans-serif;
    font-size: 88px;
    line-height: 1;
    color: var(--white);
    word-spacing: 34px;
    letter-spacing: 1px;
  }
  .vision {
    top: 248px;
    font-family: "Open Sans", sans-serif;
    font-weight: 800;
    font-size: 38px;
    color: var(--white);
    letter-spacing: 2px;
  }
  .brand {
    top: 360px;
    display: flex;
    flex-direction: column;
    align-items: center;
    gap: 34px;
  }
  .brand-dot {
    width: 170px;
    height: 170px;
    border-radius: 50%;
    background: var(--gold);
  }
  .brand-name {
    font-family: "Michroma", sans-serif;
    font-size: 46px;
    color: var(--ink);
    letter-spacing: 2px;
    line-height: 1;
  }
  .dates {
    top: 738px;
    left: -20px;
    font-family: "Michroma", sans-serif;
    font-size: 30px;
    color: var(--pink);
    letter-spacing: 9px;
  }
  .start-time {
    top: 880px;
    font-family: "PT Sans Narrow", sans-serif;
    font-weight: 700;
    font-size: 40px;
    color: var(--pink);
  }
  .venue {
    top: 1022px;
    font-family: "Cabin", sans-serif;
    font-weight: 700;
    font-size: 31px;
    color: var(--pink);
    letter-spacing: 1.5px;
    line-height: 47px;
    font-style: normal;
  }
  .venue .street {
    display: block;
    letter-spacing: 3px;
  }
</style>
</head>
<body>
  <main class="flyer">
    <h1 class="title">ANNUAL CONFERENCE</h1>
    <p class="vision">PROPHETIC, WORSHIP, PRAYER</p>
    <div class="brand">
      <span class="brand-dot"></span>
      <span class="brand-name">HARVEST LANTERN</span>
    </div>
    <p class="dates">AUGUST 24 – 26,2018</p>
    <p class="start-time">STARTING FROM 6.00PM</p>
    <address class="venue">
      <span class="place">Dunmore Community Center ( Downtown Portland)</span>
      <span class="street">482 Willowby Street, Portland, ME 04117</span>
    </address>
  </main>
</body>
</html>
```